I need a newspaper ads that suits events / outings all over the world. refreshing feeling that suits my company logo.
Size of the ads is 6cm by 6cm a square
takenote
1) Joining up as members is free .
2) Places of interest tickets discount for members
3) Special events / outings host almost everyday
4) main point is everyone able to know each another
website : www.WanderNookly.com
Target Market(s)
Targeting general age 18-40 . mainly singles
contents to put inside the ads
2) Local Places of interest tickets discount for members
4) Website : www.WanderNookly.com
5) We also host photos contest
6) Meet the different faces of the world
7) Experience Sharing Gathering !
Industry/Entity Type
It Company
Requirements
Must have
- Refreshing feeling , and professional . will be uploading more pictures , kindly put some pictures combine into it to make people feel there is a lot activities can be involve when they join as member.

```html
<!DOCTYPE html>
<html lang="en">
<head>
<meta charset="utf-8">
<title>Nookly Events – The Gate to the New World</title>
<link rel="stylesheet" href="https://fonts.googleapis.com/css2?family=Bebas+Neue&family=Lato:wght@400;700&display=swap">
<style>
  :root {
    --charcoal: #3a3a3c;
    --charcoal-deep: #2b2b2d;
    --paper: #ffffff;
    --ink: #1f1f1f;
    --bullet-blue: #2a8ac4;
    --bar-blue: #2c6f99;
    --logo-slate: #3c5a78;
  }
  html, body {
    margin: 0;
    padding: 0;
    width: 1200px;
    height: 1200px;
    overflow: hidden;
    background: var(--paper);
  }
  .ad {
    position: relative;
    width: 1200px;
    height: 1200px;
    overflow: hidden;
    background: var(--paper);
    font-family: "Lato", Arial, sans-serif;
  }
  .group-photo {
    position: absolute;
    inset: 0;
    background:
      radial-gradient(ellipse 260px 220px at 520px 470px, rgba(226,196,72,0.85), rgba(226,196,72,0) 75%),
      radial-gradient(ellipse 200px 200px at 150px 560px, rgba(196,150,120,0.55), rgba(196,150,120,0) 75%),
      radial-gradient(ellipse 220px 240px at 700px 600px, rgba(210,168,140,0.55), rgba(210,168,140,0) 75%),
      radial-gradient(ellipse 220px 260px at 1060px 600px, rgba(120,90,80,0.6), rgba(120,90,80,0) 75%),
      radial-gradient(ellipse 260px 220px at 900px 470px, rgba(90,120,110,0.6), rgba(90,120,110,0) 75%),
      linear-gradient(180deg, var(--charcoal-deep) 0%, var(--charcoal) 22%, #4a4640 40%, #6b5e52 60%, #7a7068 75%);
  }
  .fade {
    position: absolute;
    inset: 0;
    background:
      linear-gradient(180deg, rgba(255,255,255,0) 55%, rgba(255,255,255,0.75) 66%, #fff 78%),
      linear-gradient(90deg, rgba(255,255,255,0.25) 0%, rgba(255,255,255,0) 60%);
  }
  .swoosh {
    position: absolute;
    left: 0;
    top: 820px;
    width: 1200px;
    height: 380px;
  }
  .headline {
    position: absolute;
    left: 62px;
    top: 92px;
    margin: 0;
    color: var(--paper);
    font-family: "Bebas Neue", "Oswald", sans-serif;
    font-weight: 400;
    line-height: 1;
  }
  .headline .lead {
    display: block;
    font-size: 84px;
    letter-spacing: 1px;
  }
  .headline .big {
    display: block;
    font-size: 292px;
    line-height: 0.82;
    margin-top: 8px;
    letter-spacing: 2px;
  }
  .brand-badge {
    position: absolute;
    left: 867px;
    top: -12px;
    width: 288px;
    height: 288px;
    border-radius: 50%;
    background: var(--paper);
    display: flex;
    flex-direction: column;
    align-items: center;
    justify-content: center;
  }
  .brand-name {
    color: var(--logo-slate);
    font-family: "Lato", Arial, sans-serif;
    font-weight: 400;
    text-align: center;
    line-height: 1.1;
    margin-top: 40px;
  }
  .brand-name .main { display: block; font-size: 40px; letter-spacing: 2px; }
  .brand-name .sub { display: block; font-size: 22px; letter-spacing: 12px; }
  .perks {
    position: absolute;
    left: 64px;
    top: 780px;
    margin: 0;
    padding: 0;
    list-style: none;
    color: var(--ink);
  }
  .perks li {
    position: relative;
    padding-left: 58px;
    white-space: nowrap;
    line-height: 1;
  }
  .perks li::before {
    content: "";
    position: absolute;
    left: 4px;
    top: 50%;
    width: 15px;
    height: 15px;
    margin-top: -7px;
    border-radius: 50%;
    background: var(--bullet-blue);
  }
  .perks .xl { font-size: 49px; height: 57px; }
  .perks .sm { font-size: 25px; height: 54px; display: flex; align-items: center; }
  .perks .md { font-size: 38px; height: 56px; display: flex; align-items: center; }
  .perks .xl { display: flex; align-items: center; }
  .web-bar {
    position: absolute;
    left: 742px;
    top: 1148px;
    width: 456px;
    height: 36px;
    background: var(--bar-blue);
    color: var(--paper);
    font-size: 27px;
    line-height: 36px;
    text-align: center;
  }
</style>
</head>
<body>
<main class="ad">
  <div class="group-photo" role="img" aria-label="Photo of five smiling young friends posing together at the entrance of a bird park"></div>
  <div class="fade"></div>
  <svg class="swoosh" viewBox="0 0 1200 380" aria-hidden="true">
    <path d="M 0 160 C 400 60, 800 120, 1200 40" fill="none" stroke="rgba(200,200,205,0.45)" stroke-width="22"/>
    <path d="M 300 230 C 650 140, 950 170, 1200 110" fill="none" stroke="rgba(190,190,195,0.35)" stroke-width="10"/>
    <path d="M 500 300 C 800 230, 1000 240, 1200 190" fill="none" stroke="rgba(190,190,195,0.3)" stroke-width="6"/>
  </svg>

  <h1 class="headline">
    <span class="lead">The gate to the new</span>
    <span class="big">World</span>
  </h1>

  <div class="brand-badge">
    <div class="brand-name">
      <span class="main">NOOKLY</span>
      <span class="sub">EVENTS</span>
    </div>
  </div>

  <ul class="perks">
    <li class="xl">Joining up as members is free</li>
    <li class="sm">Local Places of interest tickets discount for members</li>
    <li class="sm">Special events / outings host almost everyday</li>
    <li class="xl">We also host photos contest</li>
    <li class="md">Meet the different faces of the world</li>
    <li class="xl">Experience Sharing Gathering !</li>
  </ul>

  <div class="web-bar">Website : www.WanderNookly.com</div>
</main>
</body>
</html>
```